A clean crisp business card for a Landscape Construction company. Designed to be easy to read contact/ info and also be appealing/interesting, unlike a traditional business card.

Industry/Entity Type

Landscape Construction

Contact Information for Business Card

Company name : Bramblecrest Landscape Construction, phone number: (877) 62Vales, website:Bramblecrestlandscapes.example, Email, sales@bramblecrestlandscapes.example

Requirements
Nice to have
• Luxurious finishes/ details…. Icons or emblems next to contact info
Should not have
• Clipart or general pictures

```html
<!DOCTYPE html>
<html lang="en">
<head>
<meta charset="utf-8">
<title>Bramblecrest Landscape Construction – Business Card</title>
<link rel="stylesheet" href="https://fonts.googleapis.com/css2?family=Cinzel:wght@400;600&family=Open+Sans:wght@400;600&display=swap">
<style>
  :root {
    --page: #ececec;
    --blue: #2a6fc0;
    --blue-bright: #3b82d6;
    --green: #9fcb3b;
    --black: #121212;
    --white: #ffffff;
    --muted: #e9e9e9;
  }
  * { margin: 0; padding: 0; box-sizing: border-box; }
  html, body { width: 1200px; height: 913px; overflow: hidden; background: var(--page); }
  .canvas {
    width: 1200px; height: 913px;
    display: flex; flex-direction: column; align-items: center; justify-content: center; gap: 33px;
  }
  .card {
    width: 700px; height: 400px; border-radius: 4px;
    position: relative; overflow: hidden;
    box-shadow: 0 4px 14px rgba(0,0,0,.18);
  }
  /* Front */
  .card-front {
    background: var(--blue);
    display: flex; flex-direction: column; align-items: center; justify-content: center;
    color: var(--white);
  }
  .brand-name {
    font-family: "Cinzel", serif; font-weight: 600; color: var(--white);
    text-align: center; line-height: 1.15;
    display: flex; align-items: center; gap: 14px;
  }
  .brand-mark { width: 22px; height: 22px; border-radius: 50%; background: var(--green); flex: none; }
  .brand-name .word { font-size: 48px; display: block; white-space: nowrap; }
  .brand-name .sub { font-size: 19px; letter-spacing: 4px; display: block; white-space: nowrap; }
  .front-url {
    margin-top: 44px;
    font-family: "Cinzel", serif; font-size: 17px; letter-spacing: 2px;
  }
  /* Back */
  .card-back {
    background: var(--black);
    display: flex; align-items: center;
    padding: 0 36px 0 40px;
  }
  .back-brand { width: 250px; flex: none; align-self: flex-end; margin-bottom: 110px; }
  .back-brand .brand-name { color: var(--blue-bright); gap: 10px; }
  .back-brand .brand-mark { background: var(--blue-bright); width: 16px; height: 16px; }
  .back-brand .brand-name .word { font-size: 30px; }
  .back-brand .brand-name .sub { font-size: 11px; letter-spacing: 2.4px; }
  .divider { width: 4px; height: 190px; margin: 0 26px 0 24px; display: flex; flex-direction: column; flex: none; }
  .divider span { flex: 1; }
  .divider .g { background: var(--green); width: 2px; margin-left: 1px; }
  .divider .b { background: var(--blue-bright); flex: 2; }
  .contact {
    flex: 1; min-width: 0;
    color: var(--muted); font-family: "Open Sans", sans-serif; font-size: 14px; line-height: 1.6;
  }
  .person { font-family: "Cinzel", serif; font-size: 26px; font-weight: 600; line-height: 1.1; white-space: nowrap; }
  .person .first { color: var(--blue-bright); }
  .person .last { color: var(--green); }
  .role { margin-bottom: 12px; }
  .address { margin-bottom: 10px; }
  .line { display: flex; align-items: center; gap: 9px; white-space: nowrap; }
  .line svg { width: 14px; height: 14px; flex: none; fill: var(--green); }
</style>
</head>
<body>
<main class="canvas">
  <section class="card card-front" aria-label="Card front">
    <div class="brand-name">
      <span class="brand-mark"></span>
      <span><span class="word">Bramblecrest</span><span class="sub">Landscape Construction</span></span>
    </div>
    <p class="front-url">www.Bramblecrestlandscapes.example</p>
  </section>

  <section class="card card-back" aria-label="Card back">
    <div class="back-brand">
      <div class="brand-name">
        <span class="brand-mark"></span>
        <span><span class="word">Bramblecrest</span><span class="sub">Landscape Construction</span></span>
      </div>
    </div>
    <div class="divider"><span class="g"></span><span class="b"></span><span class="g"></span></div>
    <div class="contact">
      <p class="person"><span class="first">Daniel</span> <span class="last">Hale</span></p>
      <p class="role">Director</p>
      <p class="address">4410 Maple Ridge Rd.,<br>Suite 118, Fairview, OH 45012</p>
      <p class="line"><svg viewBox="0 0 24 24"><path d="M6.6 10.8a15 15 0 0 0 6.6 6.6l2.2-2.2c.3-.3.7-.4 1-.2 1.1.4 2.3.6 3.6.6.6 0 1 .4 1 1V20c0 .6-.4 1-1 1A17 17 0 0 1 3 4c0-.6.4-1 1-1h3.5c.6 0 1 .4 1 1 0 1.3.2 2.5.6 3.6.1.3 0 .7-.2 1z"/></svg>(877) 62Vales</p>
      <p class="line"><svg viewBox="0 0 24 24"><path d="M2 5h20v14H2z M2 5l10 8 10-8"/></svg>sales@bramblecrestlandscapes.example</p>
      <p class="line"><svg viewBox="0 0 24 24"><circle cx="12" cy="12" r="10"/></svg>www.bramblecrestlandscapes.example</p>
    </div>
  </section>
</main>
</body>
</html>
```